Brixley Select Charters Flyer

Brixley Select Charters (.com) is a high end luxury and private charter company in the Cayman Islands. All info can be found on our webiste. I currently have a 4 panel roll fold flyer (Can supply working file). I am looking for a new fresh look but also need some changes as we have changes some boats, added some new charter ideas etc.

Between our website and current flyer I think the designer will get the idea. I Welcome new and fresh, I do not need it to match current website, as I may get that changed to.

We are looking for high end and simple/clean and comunicate reliability and professional with a hint of fun in the sun of course. Not whacky and tacky!!

The current PDF's of the current flyer needs a fair bit of changing (For example scuba diving panel will come out and go into a new 1 panel flyer.) I will need 3-4 other flyers too, and a bunch of other stuff in future for new businesses, but starting with this one so I can pick a designer (This is my 1st go with pixel hive, always did my own work, but am too busy and am not very good with creativity)

I have logo, support pictures, etc. Have uploaded the basics can email more info and changes after I find a designer. Lots of our boat pictures can be found at http://brixleyselectcharters.example/downloads/acorn.zip

Also, we want a panel dedicated to wavedart.example as our big boat now has one onboard and our smaller boat (23') will have two and that will be a dedicated panel (Replace scuba) offering a "Wavedart Turbo Reef trip" (I will supply more info on that, once I pick a designer).

High end groups. The groups or families that will spend more to get more!!

```html
<!DOCTYPE html>
<html lang="en">
<head>
<meta charset="utf-8">
<title>Brixley Select Charters – Roll Fold Flyer</title>
<link href="https://fonts.googleapis.com/css2?family=Cinzel:wght@700&family=Source+Sans+3:ital,wght@0,400;0,600;0,700;1,600;1,700&display=swap" rel="stylesheet">
<style>
  :root {
    --cream: #fbf8ee;
    --ink: #3a3a3a;
    --orange: #e8552a;
    --orange-deep: #e2471c;
    --amber: #f6a01f;
    --sea: #2a93bb;
    --sea-deep: #17678f;
    --sky: #9fd0ec;
    --silver: #c9c9c9;
    --black: #111;
  }
  * { margin: 0; padding: 0; box-sizing: border-box; }
  html, body { width: 1200px; height: 751px; overflow: hidden; background: var(--cream); }
  .flyer {
    position: relative; width: 1200px; height: 751px; overflow: hidden;
    background: var(--cream);
    font-family: "Source Sans 3", sans-serif; color: var(--ink);
  }
  .artwork { position: absolute; inset: 0; }
  .block { position: absolute; }
  .heading {
    font-family: "Cinzel", serif; font-weight: 700; color: var(--orange);
    letter-spacing: 1.5px; line-height: 1.25;
  }
  .brand-mark {
    display: flex; align-items: center; gap: 8px;
    font-family: "Source Sans 3", sans-serif; font-weight: 700; color: var(--black);
  }
  .brand-mark .dot { width: 14px; height: 14px; border-radius: 50%; background: var(--amber); flex: none; }

  /* left panel */
  .brand-left { left: 22px; top: 430px; font-size: 17px; }
  .contact-title { left: 22px; top: 496px; font-size: 20px; }
  .contact { left: 22px; top: 528px; font-size: 11.6px; line-height: 14.2px; color: #222; }
  .contact p + p { margin-top: 11px; }

  /* middle panel */
  .reasons-title { left: 380px; top: 178px; width: 205px; text-align: right; font-size: 19.5px; line-height: 25px; }
  .reasons { left: 309px; top: 268px; width: 282px; font-size: 10.2px; line-height: 12.6px; text-align: justify; }
  .reasons p { margin-bottom: 6px; }
  .reasons em { font-weight: 700; }
  .things-title { left: 300px; top: 537px; width: 296px; text-align: center; font-size: 18.5px; line-height: 23px; }
  .things { left: 318px; top: 598px; font-size: 10.2px; line-height: 16.6px; }
  .things ul { list-style: none; }
  .things li::before { content: "•"; display: inline-block; width: 16px; margin-left: -16px; }
  .things ul { padding-left: 16px; }
  .things-extra { left: 460px; top: 646px; font-size: 10.2px; line-height: 16.6px; }
  .things-extra ul { list-style: none; padding-left: 16px; }
  .things-extra li::before { content: "•"; display: inline-block; width: 16px; margin-left: -16px; }

  /* stingray panel */
  .ray-title { left: 620px; top: 36px; width: 268px; text-align: right; font-size: 18.5px; line-height: 25px; }
  .ray-copy { left: 609px; top: 100px; width: 280px; font-size: 10.2px; line-height: 13.1px; text-align: justify; }
  .ray-copy p { margin-bottom: 8px; }
  .ray-copy strong { font-weight: 700; }
  .ray-copy .lead { font-weight: 700; }

  .call { right: 314px; top: 721px; font-size: 20px; color: var(--ink); }
  .call b { font-style: italic; font-weight: 700; }

  /* right panel */
  .brand-right { left: 918px; top: 420px; width: 270px; flex-direction: column; gap: 6px; }
  .brand-right .name { font-size: 22px; color: var(--black); }
  .brand-right .tag { font-size: 11.5px; font-weight: 700; letter-spacing: .4px; color: var(--black); }
</style>
</head>
<body>
<main class="flyer">
  <svg class="artwork" width="1200" height="751" viewBox="0 0 1200 751">
    <defs>
      <linearGradient id="seaFade" x1="0" y1="0" x2="1" y2="1">
        <stop offset="0" stop-color="#3fb2d4"/>
        <stop offset=".55" stop-color="var(--sea)"/>
        <stop offset="1" stop-color="var(--sea-deep)"/>
      </linearGradient>
      <linearGradient id="skySea" x1="0" y1="0" x2="0" y2="1">
        <stop offset="0" stop-color="#d9ecf6"/>
        <stop offset=".5" stop-color="var(--sky)"/>
        <stop offset=".62" stop-color="#2f8fb1"/>
        <stop offset="1" stop-color="#176a8c"/>
      </linearGradient>
      <linearGradient id="deckSun" x1="0" y1="0" x2="1" y2="1">
        <stop offset="0" stop-color="#8fc6de"/>
        <stop offset=".45" stop-color="#e9eef1"/>
        <stop offset="1" stop-color="#d8c3b4"/>
      </linearGradient>
      <linearGradient id="sunset" x1="0" y1="0" x2="1" y2="0">
        <stop offset="0" stop-color="var(--orange-deep)"/>
        <stop offset=".7" stop-color="#f07a22"/>
        <stop offset="1" stop-color="var(--amber)"/>
      </linearGradient>
    </defs>

    <path d="M0 392 C220 305 330 266 402 220 C482 166 600 92 716 0" fill="none" stroke="var(--silver)" stroke-width="9"/>
    <path role="img" aria-label="Photo: two girls laughing on a rope hammock over turquoise sea spray beside a white boat hull"
          d="M0 0 H710 C600 90 480 160 400 215 C330 262 220 300 0 386 Z" fill="url(#seaFade)"/>

    <path d="M900 362 C980 306 1100 266 1200 261" fill="none" stroke="var(--black)" stroke-width="10"/>
    <path role="img" aria-label="Photo: white sport fishing boat cruising across blue water under a cloudy sky"
          d="M900 0 H1200 V254 C1100 262 980 300 900 354 Z" fill="url(#skySea)"/>

    <rect role="img" aria-label="Photo: white catamaran under sail on calm sea with clouds" x="600" y="489" width="234" height="227" fill="url(#skySea)"/>

    <path d="M306 751 C420 706 560 698 700 702 C800 706 860 686 900 634 V751 Z" fill="url(#sunset)"/>

    <path d="M900 630 C1000 552 1100 518 1200 516" fill="none" stroke="var(--silver)" stroke-width="9"/>
    <path role="img" aria-label="Photo: group of guests sunbathing on the front deck of a boat"
          d="M900 636 C1000 560 1100 525 1200 523 V751 H900 Z" fill="url(#deckSun)"/>
  </svg>

  <!-- Left panel -->
  <div class="block brand-mark brand-left"><span class="dot"></span>Brixley Select Charters</div>
  <h2 class="block heading contact-title">Contact Us</h2>
  <div class="block contact">
    <p>tel: (555) 210-4471<br>fax: (555) 210-4472<br>info@brixleyselectcharters.example<br>www.brixleyselectcharters.example</p>
    <p>tel: (555)-318-6620<br>info@lagoonlightsailing.example<br>www.lagoonlightsailing.example</p>
    <p>tel: (555) 427-9035<br>&nbsp;Fax: (555) 427-9036<br>info@harbourcrestdivers.example<br>www.harbourcrestdivers.example</p>
  </div>

  <!-- Middle panel -->
  <h2 class="block heading reasons-title">6 Great Reasons to go private:</h2>
  <div class="block reasons">
    <p><em>Uniqueness</em> - Your private boat for the day as our luxury vessels are not decorated with company logos and phone numbers. It looks and feels like your boat for the day.</p>
    <p><em>Your Comfort</em> - Your friends and family are safe from unwanted crowds and get the attention &amp; privacy you deserve..</p>
    <p><em>Your Piece of Mind</em> - Our boats and equipment are sparkling clean, elegant and well-staffed &amp; maintained.</p>
    <p><em>Value</em> - Enjoy the day, your free time is valuable, spend it on the good stuff not the stress. avoid long waiting time to get into the water, get the most out of your diving, snorkeling or playing with the stingrays.</p>
    <p><em>Your Destinations</em> - Since you are on a private charter, you decide where to go and what to do. Maybe you want more time with the stingrays, and less snorkeling, or maybe just a long relaxing lunch, the choice is yours.</p>
    <p><em>Amenities</em> - Fuel, crew, water, sodas/juices, and snacks are all included. Just come with your smile and suntan lotion.</p>
  </div>
  <h2 class="block heading things-title">Things to do with us in Grand Cayman</h2>
  <div class="block things">
    <ul>
      <li>Swimming and Snorkeling</li>
      <li>Bioluminescence Night Diving</li>
      <li>SS Marlowe Snorkelling</li>
      <li>Deep Sea Fishing</li>
      <li>Seastar Point</li>
      <li>Calloway Bbq Tuesdays</li>
      <li>Purchase a vacation home</li>
    </ul>
  </div>
  <div class="block things-extra">
    <ul>
      <li>Family Beach Portraits</li>
      <li>Rent your own vacation villa</li>
    </ul>
  </div>

  <!-- Stingray panel -->
  <h2 class="block heading ray-title">Southern Atlantic Stingrays</h2>
  <div class="block ray-copy">
    <p><strong>Female are the largest of the species,</strong> upperbody is like fine gray sand paper and the underbody smooth like silk, they don't have any teeth what they have is cartlidge, and <strong>a suction that's equivalent to 5 heavyduty vaccum cleaners.</strong> Eyes are on top, mouths are directly under the eyes at the bottom.</p>
    <p>They have a spine down its back area is very rough on the hands, some of them do have stingers, most people believe the stingers is at the end of the tail, but is not, is about 3rd the way down the tail. They only grow one stinger in its lifetime. They give life birth, The pups hatch from their egg capsules inside the mother's brood chambers, and are born soon afterwards. each creature would pop around 5 to 7 pups, as often as twice a year.... they live for about 40 years, and their top speed is about 40 miles per hour. They have sensors in their wings to detect baby octopus, small crusteceans, and any mussle that grow on shells. They ocassionally eat small fish</p>
    <p class="lead">In Grand Cayman the Stingrays Swim with divers and snorkelers as they have grown accustomed to being fed, held and caressed by humans. Most of the local Stingray handlers will teach you how to pet them, feed them squid, hold them and kiss them.</p>
    <p class="lead">Our captain Rowan will give you a "famous" stingray back or full body massage as careful as possible to avoid the abuse of the creatures..</p>
    <p>Stingrays are usually docile and curious, their usual reaction is fleeing at any disturbance.</p>
  </div>
  <div class="block call"><b>Call Us Now</b> : 555-284-1190</div>

  <!-- Right panel -->
  <div class="block brand-mark brand-right">
    <span class="dot"></span>
    <span class="name">Brixley Select Charters</span>
    <span class="tag">Yachting - Diving - Fishing - Snorkeling</span>
  </div>
</main>
</body>
</html>
```